Real Estate Team Needs Business Cards

Double sided - Team Member on Front, Team Leader on Back (back side will contain more details).
Colors to use:
Red = R: 233 G: 1 B: 2
Grey = R: 89 G: 89 B: 89
Black= R: 0 B: 0 B: 0
** MAIN FOCUS ** ( separate border, color, design, etc. to really stand out - whatever you think draws the most attention ) on both sides for "Sell for 1%‡" and "Buy & receive up to a 1% rebate‡". Must have fine print **
**Please make both sides stand out and look unique / different
Business card to have round corners (standard size 3.5" x 2").:
Document Trim Size
89 x 51 mm
1050 x 600 pixels
Full Bleed Size
92 x 54 mm
1085 x 635 pixels
Basic example provided. Please redesign as you see best. In your design - Please use the same picture on both sides. Name, address, phone number, email, etc. will be provided to the selected design. QR code on back side only if there is room (not important)

```html
<!DOCTYPE html>
<html lang="en">
<head>
<meta charset="utf-8">
<title>Harbor Point Realty – Business Cards</title>
<link rel="stylesheet" href="https://fonts.googleapis.com/css2?family=Lato:wght@400;700;900&display=swap">
<style>
  :root {
    --red: rgb(233, 1, 2);
    --grey: rgb(89, 89, 89);
    --black: rgb(0, 0, 0);
    --paper: #ffffff;
    --stage: #e4e4e6;
    --photo-top: #c9ccd3;
    --photo-bottom: #2f4f8a;
  }
  * { box-sizing: border-box; margin: 0; padding: 0; }
  html, body {
    width: 974px; height: 1200px; overflow: hidden;
    background: var(--stage);
    font-family: "Lato", Arial, sans-serif;
  }
  .canvas { position: relative; width: 974px; height: 1200px; }
  .card {
    position: absolute; background: var(--paper);
    box-shadow: 0 6px 18px rgba(0,0,0,0.18);
    overflow: hidden;
  }
  .card--front { left: 43px; top: 52px; width: 882px; height: 517px; }
  .card--back  { left: 51px; top: 645px; width: 874px; height: 512px; }
  .abs { position: absolute; }
  .text { z-index: 2; white-space: nowrap; }

  .contact-labels { color: var(--red); font-weight: 700; font-size: 21px; line-height: 26px; }
  .promo { color: var(--red); font-weight: 700; font-size: 30px; line-height: 31px; }
  .person-name { color: var(--black); font-weight: 700; font-size: 30px; line-height: 34px; letter-spacing: -0.3px; }
  .person-role { color: var(--grey); font-size: 22px; line-height: 26px; }
  .photo {
    z-index: 1;
    background: linear-gradient(180deg, var(--photo-top) 0%, #a9b2c2 40%, var(--photo-bottom) 65%, #223e72 100%);
  }
  .rule { height: 5px; }
  .rule--red { background: var(--red); }
  .rule--black { background: var(--black); }
  .brand {
    display: flex; align-items: center; gap: 12px;
    color: var(--black); font-weight: 900; font-size: 36px; line-height: 40px; letter-spacing: 0.5px;
    white-space: nowrap; transform: translateX(-50%);
  }
  .brand__mark { width: 22px; height: 22px; background: var(--red); }
  .website {
    color: var(--red); font-weight: 700; font-size: 22px; line-height: 26px;
    transform: translateX(-50%); white-space: nowrap;
  }
  .team-title {
    left: 0; width: 100%; text-align: center;
    color: var(--black); font-weight: 700; font-size: 34px; line-height: 40px;
  }
  .services { font-size: 24px; line-height: 30px; font-weight: 700; list-style: none; }
  .services .is-promo { color: var(--red); }
  .services .is-feature { color: var(--black); }
</style>
</head>
<body>
<main class="canvas">

  <section class="card card--front" aria-label="Front of card – team member">
    <div class="abs text contact-labels" style="left:43px; top:44px;">
      <div>Cell:</div><div>Office:</div><div>E-mail:</div>
    </div>
    <div class="abs text promo" style="left:363px; top:46px;">
      <div>Sell For 1%</div>
      <div>Buy &amp; receive up to a 1% rebate</div>
    </div>
    <div class="abs text person-name" style="left:139px; top:170px;">EMPLOYEE NAME</div>
    <div class="abs text person-role" style="left:233px; top:206px;">Position</div>

    <div class="abs photo" role="img" aria-label="Portrait photo of the team member in a navy suit" style="left:0; top:248px; width:227px; height:269px;"></div>

    <div class="abs rule rule--red" style="left:227px; top:349px; width:655px;"></div>
    <div class="abs rule rule--black" style="left:227px; top:358px; width:655px; height:4px;"></div>

    <div class="abs text brand" style="left:548px; top:376px;">
      <span class="brand__mark"></span><span>HARBOR POINT REALTY</span>
    </div>

    <div class="abs rule rule--black" style="left:227px; top:456px; width:655px;"></div>
    <div class="abs text website" style="left:547px; top:472px;">www.website.com</div>
  </section>

  <section class="card card--back" aria-label="Back of card – team leader">
    <div class="abs text team-title" style="top:44px;">Harbor Point Real Estate Team</div>
    <div class="abs text contact-labels" style="left:46px; top:104px;">
      <div>Address:</div><div>Office:</div><div>E-mail:</div>
    </div>
    <div class="abs text person-name" style="left:42px; top:194px;">OWNER NAME</div>
    <div class="abs text person-role" style="left:185px; top:228px;">Position</div>

    <div class="abs photo" role="img" aria-label="Portrait photo of the team leader in a navy suit" style="left:0; top:266px; width:225px; height:246px;"></div>

    <div class="abs text brand" style="left:605px; top:205px;">
      <span class="brand__mark"></span><span>HARBOR POINT REALTY</span>
    </div>

    <ul class="abs text services" style="left:384px; top:286px;">
      <li class="is-promo">Sell For 1%</li>
      <li class="is-promo">Buy &amp; receive up to a 1% rebate</li>
      <li class="is-feature">Free home evaluation</li>
      <li class="is-feature">Free local sold reports</li>
      <li class="is-feature">Advanced Propery Search</li>
    </ul>

    <div class="abs rule rule--black" style="left:225px; top:449px; width:649px;"></div>
    <div class="abs text website" style="left:605px; top:464px;">www.website.com</div>
  </section>

</main>
</body>
</html>
```